Need Letterhead & Stationery for Construction Company

Hello,
I have a small construction company that I recently started. I already have the logo but I want to create a letterhead, stationery and business cards for it. I want an elegant design which should feel like a corporate company. Kindly let me know what else you need from my end to start with the design.
I also need digital copies of letterhead so that I can send PDF's directly to clients.

** logo attached, colors I would like to stay in Grey / Shades of Red

** Details required in Business Card:
Name, Designation, Mobile, Telephone, Email, other email, POBOX, Address, website

Requirements
Should not have
• funky styles, too many colors.

```html
<!DOCTYPE html>
<html lang="en">
<head>
<meta charset="utf-8">
<title>Corvane Steel Works – Business Card</title>
<link rel="stylesheet" href="https://fonts.googleapis.com/css2?family=Montserrat:wght@500;600;700&family=Roboto:wght@400;500&display=swap">
<style>
  :root {
    --bg: #1c1c1c;
    --card-dark-1: #5a5a5a;
    --card-dark-2: #2e2e2e;
    --white: #ffffff;
    --ink: #141414;
    --red: #e4261f;
    --band: #0d0d0d;
    --text-grey: #3a3a3a;
  }
  * { box-sizing: border-box; margin: 0; padding: 0; }
  html, body { width: 1200px; height: 929px; overflow: hidden; background: var(--bg); }
  .stage { position: relative; width: 1200px; height: 929px; }

  .card {
    position: absolute; left: 250px; width: 700px; height: 400px;
    overflow: hidden; box-shadow: 0 12px 30px rgba(0,0,0,.5);
  }

  /* Back of card */
  .card--back { top: 40px; background: var(--card-dark-2); }
  .card--back .building-art {
    position: absolute; inset: 0;
    background: linear-gradient(135deg, var(--card-dark-1) 0%, #474747 45%, var(--card-dark-2) 100%);
  }
  .card--back .brand { position: absolute; left: 150px; top: 150px; color: var(--white); }

  .brand { display: flex; align-items: center; gap: 18px; font-family: "Montserrat", sans-serif; font-weight: 600; }
  .brand__dot { border-radius: 50%; background: currentColor; flex: none; }
  .brand__name { line-height: 1; letter-spacing: .12em; }
  .brand__tag { display: block; letter-spacing: .06em; margin-top: 6px; }
  .card--back .brand__dot { width: 90px; height: 90px; }
  .card--back .brand__name { font-size: 64px; }
  .card--back .brand__tag { font-size: 13px; }

  /* Front of card */
  .card--front { top: 489px; background: var(--white); }
  .card--front .brand { position: absolute; right: 40px; top: 40px; color: var(--ink); gap: 12px; }
  .card--front .brand__dot { width: 46px; height: 46px; }
  .card--front .brand__name { font-size: 34px; }
  .card--front .brand__tag { font-size: 7.5px; margin-top: 4px; }

  .person { position: absolute; left: 46px; top: 170px; }
  .person__name { font-family: "Montserrat", sans-serif; font-weight: 700; font-size: 22px; color: var(--ink); letter-spacing: .02em; }
  .person__role { font-family: "Roboto", sans-serif; font-size: 20px; color: var(--red); margin-top: 2px; }

  .contacts { position: absolute; left: 46px; top: 240px; list-style: none; font-family: "Roboto", sans-serif; font-size: 19px; color: var(--text-grey); }
  .contacts li { display: flex; align-items: center; gap: 10px; height: 24px; }
  .contacts svg { width: 16px; height: 16px; fill: var(--red); flex: none; }

  .address-band {
    position: absolute; left: 0; right: 0; bottom: 22px; height: 42px;
    background: var(--band); display: flex; align-items: center; padding-left: 40px; gap: 10px;
    font-family: "Roboto", sans-serif; font-size: 20px; color: var(--white);
  }
  .address-band svg { width: 16px; height: 20px; fill: var(--red); }
  .address-band::after {
    content: ""; position: absolute; right: 0; top: 0; width: 80px; height: 100%; background: var(--red);
  }
</style>
</head>
<body>
<main class="stage">
  <section class="card card--back">
    <div class="building-art" role="img" aria-label="Line drawing of a multi-storey building in faint grey strokes"></div>
    <div class="brand">
      <span class="brand__dot"></span>
      <div>
        <span class="brand__name">CORVANE</span>
        <span class="brand__tag">STEEL WORKS CONTRACTING LLC</span>
      </div>
    </div>
  </section>

  <section class="card card--front">
    <div class="brand">
      <span class="brand__dot"></span>
      <div>
        <span class="brand__name">CORVANE</span>
        <span class="brand__tag">STEEL WORKS CONTRACTING LLC</span>
      </div>
    </div>

    <div class="person">
      <p class="person__name">MARCUS ELLERY</p>
      <p class="person__role">Managing Director</p>
    </div>

    <ul class="contacts">
      <li><svg viewBox="0 0 16 16"><path d="M4 0h8a1 1 0 0 1 1 1v14a1 1 0 0 1-1 1H4a1 1 0 0 1-1-1V1a1 1 0 0 1 1-1zm1 2v10h6V2zm3 11a1 1 0 1 0 0 2 1 1 0 0 0 0-2z"/></svg>555.210.4837</li>
      <li><svg viewBox="0 0 16 16"><path d="M1 5c0-2 3-3 7-3s7 1 7 3v1h-4V5H5v1H1zm3 2h8l2 8H2z"/></svg>555.210.9902</li>
      <li><svg viewBox="0 0 16 16"><path d="M0 3h16v10H0zm1.5 1.2L8 9l6.5-4.8V3.5h-13z"/></svg>hello@corvanemail.com</li>
      <li><svg viewBox="0 0 16 16"><circle cx="8" cy="8" r="8"/></svg>www.corvaneweb.com</li>
    </ul>

    <div class="address-band">
      <svg viewBox="0 0 16 20"><path d="M8 0a7 7 0 0 1 7 7c0 5-7 13-7 13S1 12 1 7a7 7 0 0 1 7-7zm0 4a3 3 0 1 0 0 6 3 3 0 0 0 0-6z"/></svg>
      48 Birchwood Lane, Maple Grove, ON K2T 5R1
    </div>
  </section>
</main>
</body>
</html>
```